Save the date for wedding

A save the date for our wedding. We're looking for a simple and sleek invite. I would prefer not alot of calligraphy. Minimalism is good. The basic info to include is as follows:
Names: Mona and Felix
Date: June 9th
Where: Ottawa, Ontario
In small print please include that there will be a reception in Edmonton AB September 1st for those who cannot make it to Ottawa.
Please see the attached file for a style idea. Doesn’t have to be exactly like that, but something like that.

```html
<!DOCTYPE html>
<html lang="en">
<head>
<meta charset="UTF-8">
<title>Save the Date – Mona &amp; Felix</title>
<link rel="stylesheet" href="https://fonts.googleapis.com/css2?family=Amatic+SC:wght@400;700&family=Sofia&display=swap">
<style>
  :root {
    --page-bg: #ebe5d9;
    --card-light: #fbfce4;
    --card-base: #f4f6c6;
    --ink: #231f20;
    --sprig-tone: #d9dbb0;
  }
  * { margin: 0; padding: 0; box-sizing: border-box; }
  html, body {
    width: 1200px; height: 1200px; overflow: hidden;
    background: var(--page-bg);
  }
  .card {
    position: absolute; left: 50px; top: 212px;
    width: 1100px; height: 776px;
    background: radial-gradient(ellipse at 52% 50%, var(--card-light) 0%, var(--card-base) 75%);
    color: var(--ink);
    font-family: "Amatic SC", sans-serif;
  }
  .card__frame {
    position: absolute; left: 21px; top: 16px; right: 19px; bottom: 15px;
    border: 3px solid var(--ink);
  }
  .script {
    position: absolute; font-family: "Sofia", cursive; line-height: 1; white-space: nowrap;
  }
  .script--save { left: 296px; top: 20px; font-size: 170px; }
  .script--the  { left: 590px; top: 160px; font-size: 76px; }
  .script--date { left: 470px; top: 214px; font-size: 170px; }
  .floral {
    position: absolute; background: var(--sprig-tone); border-radius: 40% 50% 45% 55%;
  }
  .floral--right { left: 692px; top: 72px; width: 235px; height: 139px; transform: rotate(-8deg); }
  .floral--left  { left: 164px; top: 220px; width: 241px; height: 144px; transform: rotate(8deg); }
  .corner-sprig {
    position: absolute; width: 58px; height: 58px; background: var(--sprig-tone); border-radius: 50%;
  }
  .corner-sprig--tl { left: 28px; top: 22px; }
  .corner-sprig--tr { right: 26px; top: 22px; }
  .corner-sprig--bl { left: 28px; bottom: 22px; }
  .corner-sprig--br { right: 26px; bottom: 22px; }
  .couple {
    position: absolute; left: 0; width: 100%; top: 418px;
    text-align: center; font-weight: 700; font-size: 104px; line-height: 1; white-space: nowrap;
  }
  .couple span { display: inline-block; }
  .couple__first { transform: rotate(-5deg) translateY(8px); }
  .couple__amp { margin: 0 14px; }
  .couple__second { transform: rotate(5deg) translateY(8px); }
  .details { position: absolute; left: 0; width: 100%; text-align: center; line-height: 1; }
  .details--lead  { top: 542px; font-size: 36px; font-weight: 400; }
  .details--date  { top: 578px; font-size: 86px; font-weight: 700; }
  .details--place { top: 660px; font-size: 30px; font-weight: 400; }
  .details--note  { top: 724px; font-size: 20px; font-weight: 400; }
</style>
</head>
<body>
  <main class="card">
    <div class="card__frame"></div>

    <div class="corner-sprig corner-sprig--tl" role="img" aria-label="Small hand-drawn leafy sprig"></div>
    <div class="corner-sprig corner-sprig--tr" role="img" aria-label="Small hand-drawn leafy sprig"></div>
    <div class="corner-sprig corner-sprig--bl" role="img" aria-label="Small hand-drawn leafy sprig"></div>
    <div class="corner-sprig corner-sprig--br" role="img" aria-label="Small hand-drawn leafy sprig"></div>

    <div class="floral floral--right" role="img" aria-label="Line-drawn floral branch"></div>
    <div class="floral floral--left" role="img" aria-label="Line-drawn floral branch"></div>

    <h1>
      <span class="script script--save">Save</span>
      <span class="script script--the">the</span>
      <span class="script script--date">Date</span>
    </h1>

    <p class="couple">
      <span class="couple__first">Mona</span><span class="couple__amp">&amp;</span><span class="couple__second">Felix</span>
    </p>

    <p class="details details--lead">are getting married on</p>
    <p class="details details--date">June 9th</p>
    <p class="details details--place">Ottawa, Ontario</p>
    <p class="details details--note">reception in Edmonton AB September 1st for those who cannot make it to Ottawa</p>
  </main>
</body>
</html>
```